Design for sports training app

We need the design for 9 screens of an app that supports trainers of sport teams in preparing their training sessions. Regarding colors, fonts etc. there is absolute freedom for the designer to choose what he thinks is best.
The app will be called "Plomix", our idea for the logo is something like a stopwatch.
Wireframes are attached for every screen. You don't have to stick to those - if you have better ideas, we are happy to see them.
Our strategy is "mobile first". Based on the app design we will create a homepage later - I guess it makes sense to give this to the same person, let's see.
The deliverables are attached.
All in all the main target is to present a very simple, intuitive and nice UI that the user can work with without much learning.
Updates
Target Market(s)
Soccer trainers
Industry/Entity Type
Training
Look and feel

```html
<!DOCTYPE html>
<html lang="en">
<head>
<meta charset="utf-8">
<title>Plomix – Training Screens</title>
<link rel="stylesheet" href="https://fonts.googleapis.com/css2?family=Oswald:wght@300;400;500&family=Inter:wght@400;500&display=swap">
<style>
  :root{
    --page:#efefef;
    --screen:#1d1f22;
    --panel:#25272b;
    --card:#27292d;
    --gap:#17181b;
    --text:#e6e7e9;
    --muted:#9a9ea4;
    --dim:#3a3d42;
    --cyan:#2fd3ea;
    --cyan-deep:#1b8fd0;
    --red:#f2201f;
    --green:#21d58a;
  }
  *{box-sizing:border-box;margin:0;padding:0}
  html,body{width:1200px;height:1200px;overflow:hidden;background:var(--page)}
  body{position:relative;font-family:"Oswald",sans-serif;color:var(--text)}
  .screen{position:absolute;top:222px;width:430px;height:756px;background:var(--screen);overflow:hidden}
  .screen--home{left:103px}
  .screen--session{left:670px}

  .status-bar{position:absolute;left:0;top:0;width:100%;height:32px;background:#1a1b1e;font-family:"Inter",sans-serif;font-size:12px;color:#fff;display:flex;align-items:center;justify-content:space-between;padding:0 14px}
  .status-bar .carrier{display:flex;align-items:center;gap:4px}
  .status-bar .battery{display:flex;align-items:center;gap:5px}
  .battery-cell{width:26px;height:11px;border:1px solid #fff;border-radius:2px;padding:1px}
  .battery-cell span{display:block;width:100%;height:100%;background:#fff}

  .app-header{position:absolute;left:0;top:32px;width:100%;height:58px;background:var(--panel);display:flex;align-items:center;justify-content:center;font-size:21px;letter-spacing:.3px}
  .app-header .settings{position:absolute;right:24px;top:16px}
  .app-header .back{position:absolute;left:28px;top:18px}

  .info-card{position:absolute;top:118px;height:117px;background:var(--card)}
  .info-card--date{left:35px;width:176px}
  .info-card--weather{left:224px;width:176px}
  .big-time{position:absolute;left:23px;top:8px;font-size:37px;font-weight:400;line-height:1.2}
  .day-box{position:absolute;left:25px;top:62px;width:43px;height:42px;border:2px solid var(--text);font-size:28px;text-align:center;line-height:36px}
  .day-box::before{content:"";position:absolute;left:0;right:0;top:0;height:4px;background:var(--text)}
  .month{position:absolute;left:82px;top:58px;font-size:22px}
  .weekday{position:absolute;left:82px;top:90px;font-size:14px;font-weight:300}
  .temp{position:absolute;left:90px;top:8px;font-size:37px}
  .cond{position:absolute;left:13px;top:56px;font-size:22px}
  .cond small{font-size:14px;font-weight:300;margin-left:8px}
  .precip{position:absolute;left:11px;top:89px;font-size:14px;font-weight:300}

  .start-button{position:absolute;left:139px;top:260px;width:156px;height:156px;border-radius:50%;border:1.5px solid var(--cyan);background:radial-gradient(circle,#20252b 0%,#1b1d21 75%);box-shadow:0 0 0 6px #1f2226;display:flex;align-items:center;justify-content:center;font-size:24px;font-weight:500;color:var(--cyan);letter-spacing:1px}

  .drill-list{position:absolute;left:6px;top:442px;width:419px}
  .drill-row{position:relative;height:64px;margin-bottom:3px;background:var(--panel)}
  .drill-row .name{position:absolute;left:37px;top:8px;font-size:22px;line-height:1.15}
  .drill-row .name em{font-style:normal;font-size:17px}
  .drill-row .dur{position:absolute;left:37px;top:37px;font-size:15px;color:var(--muted)}
  .drill-row .icon{position:absolute;right:28px;top:18px}
  .skills-row{position:absolute;left:6px;top:710px;width:419px;height:60px;background:var(--panel)}
  .skills-row .name{position:absolute;left:37px;top:9px;font-size:22px}
  .skills-row .icon{position:absolute;right:32px;top:11px}

  .session-list{position:absolute;left:6px;top:94px;width:419px}
  .session-row{position:relative;height:64px;margin-bottom:3px;background:var(--panel)}
  .session-row .name{position:absolute;left:36px;top:8px;font-size:22px}
  .session-row .name em{font-style:normal;font-size:17px}
  .session-row .dur{position:absolute;left:36px;top:37px;font-size:15px;color:var(--muted)}
  .session-row .clock{position:absolute;right:54px;top:14px;font-size:30px}
  .session-row .chev{position:absolute;right:40px;top:20px}
  .session-row .tick{position:absolute;right:85px;top:20px}
  .session-row--late .clock{color:var(--red)}
  .session-row--active .name,.session-row--active .dur,.session-row--active .clock{color:var(--cyan)}
  .session-row--pending{background:#222428}
  .session-row--pending .name,.session-row--pending .dur,.session-row--pending .clock{color:var(--dim)}

  .drill-title{position:absolute;left:0;width:100%;top:374px;text-align:center;font-size:29px;font-weight:500}
  .drill-title em{font-style:normal;font-size:23px}
  .tactics-board{position:absolute;left:116px;top:427px;width:196px;height:127px;background:linear-gradient(135deg,#2a2d32,#1f2125);border:1px solid #8b8f95}
  .drill-text{position:absolute;left:44px;top:568px;width:342px;font-size:14px;font-weight:300;line-height:18.5px;text-align:justify;color:#d6d8db}
  .finish-button{position:absolute;left:44px;top:673px;width:342px;height:54px;border:1.5px solid #a8abb0;border-radius:20px;display:flex;align-items:center;justify-content:center;font-size:21px;font-weight:300;letter-spacing:.5px}
</style>
</head>
<body>

<section class="screen screen--home">
  <div class="status-bar">
    <span class="carrier">●●●○○ NOVA
      <svg width="13" height="10" viewBox="0 0 13 10"><path d="M1 3.5a8 8 0 0 1 11 0M3 5.8a5 5 0 0 1 7 0M6.5 9l1.6-1.6a2.3 2.3 0 0 0-3.2 0z" fill="none" stroke="#fff" stroke-width="1.4"/></svg>
    </span>
    <span>4:21 PM</span>
    <span class="battery">
      <svg width="8" height="12" viewBox="0 0 8 12"><path d="M1 3l6 5-3 3V1l3 3-6 5" fill="none" stroke="#888" stroke-width="1"/></svg>
      100% <span class="battery-cell"><span></span></span>
    </span>
  </div>
  <header class="app-header">SV LINDENFELD-JUNIORS
    <svg class="settings" width="26" height="26" viewBox="0 0 26 26"><g fill="#c9cbce"><circle cx="13" cy="13" r="8"/><g stroke="#c9cbce" stroke-width="4"><path d="M13 1v5M13 20v5M1 13h5M20 13h5M4.5 4.5l3.5 3.5M18 18l3.5 3.5M4.5 21.5L8 18M18 8l3.5-3.5"/></g></g><circle cx="13" cy="13" r="3.5" fill="var(--panel)"/></svg>
  </header>

  <div class="info-card info-card--date">
    <div class="big-time">17:30 PM</div>
    <div class="day-box">15</div>
    <div class="month">MAY</div>
    <div class="weekday">SATURDAY</div>
  </div>
  <div class="info-card info-card--weather">
    <svg style="position:absolute;left:14px;top:6px" width="70" height="46" viewBox="0 0 70 46"><path d="M12 44a11 11 0 0 1 0-22 17 17 0 0 1 32-6 13 13 0 0 1 18 12 8 8 0 0 1 0 16z" fill="#8e9196"/></svg>
    <div class="temp">22°C</div>
    <div class="cond">CLEAR<small>FEEL LIKE 21°C</small></div>
    <div class="precip">PRECIPITATION: 0%</div>
  </div>

  <div class="start-button">PLOMIX</div>

  <div class="drill-list">
    <div class="drill-row"><div class="name">WARM UP</div><div class="dur">20 MINUTE</div>
      <svg class="icon" width="28" height="28" viewBox="0 0 28 28"><path d="M4 12A10 10 0 0 1 22 7M24 16A10 10 0 0 1 6 21" fill="none" stroke="#c9cbce" stroke-width="3"/><path d="M23 2v7h-7M5 26v-7h7" fill="none" stroke="#c9cbce" stroke-width="3"/></svg></div>
    <div class="drill-row"><div class="name">4 <em>vs</em> 2</div><div class="dur">25 MINUTE</div>
      <svg class="icon" width="28" height="28" viewBox="0 0 28 28"><path d="M4 12A10 10 0 0 1 22 7M24 16A10 10 0 0 1 6 21" fill="none" stroke="#c9cbce" stroke-width="3"/><path d="M23 2v7h-7M5 26v-7h7" fill="none" stroke="#c9cbce" stroke-width="3"/></svg></div>
    <div class="drill-row"><div class="name">OFFENSIVE 2 <em>vs</em> 1</div><div class="dur">25 MINUTE</div>
      <svg class="icon" width="28" height="28" viewBox="0 0 28 28"><path d="M4 12A10 10 0 0 1 22 7M24 16A10 10 0 0 1 6 21" fill="none" stroke="#c9cbce" stroke-width="3"/><path d="M23 2v7h-7M5 26v-7h7" fill="none" stroke="#c9cbce" stroke-width="3"/></svg></div>
    <div class="drill-row"><div class="name">GAME 7 ON 7</div><div class="dur">50 MINUTE</div>
      <svg class="icon" width="28" height="28" viewBox="0 0 28 28"><path d="M4 12A10 10 0 0 1 22 7M24 16A10 10 0 0 1 6 21" fill="none" stroke="#c9cbce" stroke-width="3"/><path d="M23 2v7h-7M5 26v-7h7" fill="none" stroke="#c9cbce" stroke-width="3"/></svg></div>
  </div>
  <div class="skills-row"><div class="name">PLOMIX SKILLS</div>
    <svg class="icon" width="14" height="24" viewBox="0 0 14 24"><path d="M2 2l10 10-10 10" fill="none" stroke="#c9cbce" stroke-width="2.5"/></svg></div>
</section>

<section class="screen screen--session">
  <div class="status-bar">
    <span class="carrier">●●●○○ NOVA
      <svg width="13" height="10" viewBox="0 0 13 10"><path d="M1 3.5a8 8 0 0 1 11 0M3 5.8a5 5 0 0 1 7 0M6.5 9l1.6-1.6a2.3 2.3 0 0 0-3.2 0z" fill="none" stroke="#fff" stroke-width="1.4"/></svg>
    </span>
    <span>4:21 PM</span>
    <span class="battery">
      <svg width="8" height="12" viewBox="0 0 8 12"><path d="M1 3l6 5-3 3V1l3 3-6 5" fill="none" stroke="#888" stroke-width="1"/></svg>
      100% <span class="battery-cell"><span></span></span>
    </span>
  </div>
  <header class="app-header">15 MAY&nbsp;&nbsp;17:30 UHR
    <svg class="back" width="14" height="24" viewBox="0 0 14 24"><path d="M12 2L2 12l10 10" fill="none" stroke="#c9cbce" stroke-width="2.5"/></svg>
  </header>

  <div class="session-list">
    <div class="session-row"><div class="name">WARM UP</div><div class="dur">20 MINUTE</div>
      <svg class="tick" width="36" height="26" viewBox="0 0 36 26"><path d="M3 13l10 10L33 3" fill="none" stroke="var(--green)" stroke-width="4"/></svg>
      <svg class="chev" width="14" height="26" viewBox="0 0 14 26"><path d="M2 2l10 11-10 11" fill="none" stroke="var(--green)" stroke-width="2.5"/></svg></div>
    <div class="session-row session-row--late"><div class="name">4 <em>vs</em> 2</div><div class="dur">25 MINUTE</div>
      <div class="clock">04:49</div>
      <svg class="chev" width="14" height="26" viewBox="0 0 14 26"><path d="M2 2l10 11-10 11" fill="none" stroke="var(--red)" stroke-width="2.5"/></svg></div>
    <div class="session-row session-row--active"><div class="name">OFFENSIVE 2 <em>vs</em> 1</div><div class="dur">25 MINUTE</div>
      <div class="clock">19:34</div>
      <svg class="chev" width="14" height="26" viewBox="0 0 14 26"><path d="M2 2l10 11-10 11" fill="none" stroke="var(--cyan)" stroke-width="2.5"/></svg></div>
    <div class="session-row session-row--pending"><div class="name">GAME 7 ON 7</div><div class="dur">50 MINUTE</div>
      <div class="clock">00:00</div>
      <svg class="chev" width="14" height="26" viewBox="0 0 14 26"><path d="M2 2l10 11-10 11" fill="none" stroke="var(--dim)" stroke-width="2.5"/></svg></div>
  </div>

  <h2 class="drill-title">OFFENSIVE 2 <em>vs</em> 1</h2>
  <div class="tactics-board" role="img" aria-label="Tactical diagram of the offensive 2 vs 1 drill on a football pitch"></div>
  <p class="drill-text">Praesent malesuada feugiat lacus sed ullamcorper. Cras sodales pellentesque nunc eget consectetur. Praesent non semper neque. Sed tincidunt, ante non tincidunt ullamcorper, dolor odio placerat ligula, vel eleifend felis est vitae risus.</p>
  <div class="finish-button">FINISH TRAINING</div>
</section>

</body>
</html>
```